Manufacturing business needs a website revamp

We are a manufacturing business supplying parts and modules to mid-high end consumer electronics brands from kitchen appliances to powered tools mainly in US/Europe. We want design ideas for a revamp of our website. We're aiming for a look and feel that's sleek, tidy and modern whilst still providing the right balance for content. A smooth and comfortable user experience that directs users to the information they may be looking for and promote our services. Something that incorporates design ideas such as: responsive design, lazy loading, slider banners, responsive layout, dynamic scrolling, liquid layout, full page headers etc... These are just terms bounced around within our team and certainly neither exclusive nor absolutely necessary. This is our current website for reference: https://www.valmoriqtech.com/ , which we feel is both outdated and doesn't engage visitors.

Attached is our planned new site map (we’re open to additional ideas here). We would like mock ups for each page on the site map. We will subsequently fill out the contents ourselves, but require design directions on e.g. how much text should go at which spot. E.g. for our Automotive page under Industries, we would like a suitable layout to be designed, as well as designated areas for texts. As for assets, please use any of the assets already on our current site or external source. We’ve yet to finalize on our selection of assets so please use the above as placeholders for now. Additionally, we would want a mock up for a pop-up frame to showcase additional technical specifications for some of our product ranges. For example, under the powertools section of our current website, we have additional listings under our product range. Currently they do not have a pop up function, but if we were to create a pop up frame to display detailed specifications, what layout should we use?

Finally, our target audiences are professional representatives from leading consumer brands who may be interested in our services. Our target customers are mid-high end brands. Think, for example, KRV/Halvorne for automotive, Quenmatic/Pruvet/Tolvaro for consumer electronics/kitchen appliances, and Marwick Fenn & Toller/Caddowin for powered tools. Typically it will be their product designers/engineers and supply chain representatives who will visit our website.

Target Market(s)

Professional product engineers/designers from mid-high end consumer electronics brands.

Industry/Entity Type

Manufacturing

Contact Information for Business Card

Attached are back and front of our current name card design. Again, we're open to changes that matches the style of our future website design. A few notes on the business card design:
- Cannot have blue background
- Does not have to be bilingual. I.e. open to single language design on one side and logo on the other

Coding

Coded - Design and coding required

Number of Pages Required

5+ page

Font styles to use
Sans Serif

Colors
3176b5

Requirements
Must have
• Color scheme must be based on the blue from our current website design. We will be keeping our current logo, hence must match that logo.
Nice to have
• Wix (or similar platforms) as demos/final solutions ok.
Should not have
• See brief

```html
<!DOCTYPE html>
<html lang="en">
<head>
<meta charset="utf-8">
<title>Valmoriq – Powering You Up For Success</title>
<link href="https://fonts.googleapis.com/css2?family=Poppins:wght@300;400;500;600;700&family=Open+Sans:wght@400;600&display=swap" rel="stylesheet">
<style>
:root{
  --blue:#3176b5;
  --blue-dark:#25609a;
  --ink:#1e2630;
  --muted:#6f7680;
  --line:#e3e7ec;
  --backdrop:#2a2a2a;
  --footer:#23272e;
  --white:#ffffff;
}
*{margin:0;padding:0;box-sizing:border-box}
html,body{width:1200px;height:5102px;overflow:hidden}
body{background:var(--backdrop);font-family:"Poppins",sans-serif;color:var(--ink)}
.site{position:absolute;left:50px;top:478px;width:1100px;height:4145px;background:var(--white);overflow:hidden}
.sec{position:absolute;left:0;width:1100px}
.wrap{position:absolute;left:103px;width:895px}

/* top bar */
.topbar{top:0;height:40px;background:var(--blue);color:var(--white);font-size:11px;display:flex;align-items:center;padding:0 103px;gap:26px}
.topbar .item{display:flex;align-items:center;gap:6px}
.topbar .links{margin-left:auto;display:flex;gap:8px}
.topbar .links span.sep{opacity:.6}

/* header */
.header{top:40px;height:81px;background:var(--white)}
.brand{position:absolute;left:103px;top:14px;display:flex;align-items:center;gap:10px}
.brand .mark{width:34px;height:34px;background:var(--blue)}
.brand .name{font-size:30px;font-weight:600;color:var(--ink);line-height:1}
.brand small{display:block;font-size:8px;color:var(--muted);font-weight:400;margin-top:3px}
.phone{position:absolute;right:102px;top:22px;display:flex;gap:12px;align-items:center}
.phone .lab{font-size:10px;color:var(--muted)}
.phone .num{font-size:12px;font-weight:500}

/* nav */
.nav{position:absolute;left:103px;top:121px;width:895px;height:44px;background:var(--blue);z-index:3;display:flex;align-items:center;padding:0 32px;gap:44px;color:var(--white);font-size:10px;letter-spacing:.3px}
.nav .quote{margin-left:auto;display:flex;gap:6px;align-items:center}

/* hero */
.hero{top:141px;height:530px;background:linear-gradient(135deg,#5b7690 0%,#8ba3b8 45%,#b9c8d3 70%,#6f899d 100%);clip-path:polygon(0 0,100% 0,100% 86%,0 100%)}
.hero .shade{position:absolute;inset:0;background:linear-gradient(90deg,rgba(20,32,48,.55),rgba(20,32,48,.1))}
.hero h1{position:absolute;left:103px;top:146px;color:var(--white);font-weight:300;font-size:36px;line-height:46px}
.hero h1 b{font-weight:700}
.hero p{position:absolute;left:103px;top:288px;width:500px;color:var(--white);font-family:"Open Sans",sans-serif;font-size:12px;line-height:25px}
.btn{display:inline-flex;align-items:center;gap:10px;background:var(--blue);color:var(--white);font-size:12px;height:38px;padding:0 34px;justify-content:center}
.hero .btn{position:absolute;left:103px;top:361px;width:158px}
.hero .play{position:absolute;left:283px;top:357px;display:flex;gap:14px;align-items:center;color:var(--white);font-size:11px;font-style:italic;line-height:15px}
.hero .play .c{width:46px;height:46px;border-radius:50%;background:rgba(255,255,255,.2);display:flex;align-items:center;justify-content:center}
.arrowc{position:absolute;width:36px;height:36px;border-radius:50%;border:1px solid rgba(255,255,255,.6);display:flex;align-items:center;justify-content:center;top:374px}

/* about */
.about{top:671px;height:500px}
.kicker{font-size:10px;font-weight:600;color:var(--blue);letter-spacing:.3px}
.about .left{position:absolute;left:120px;top:92px;display:flex;gap:20px}
.about h2{font-size:25px;font-weight:600;line-height:30px;margin-top:6px}
.about .right{position:absolute;left:433px;top:80px;width:420px}
.about .lead{font-size:24px;font-weight:400;line-height:36px}
.about .lead b{color:var(--blue);font-weight:600}
.about .body{font-family:"Open Sans",sans-serif;font-size:11px;color:var(--muted);line-height:22px;margin-top:18px}
.vm{display:flex;gap:100px;margin-top:24px}
.vm .col{display:flex;gap:14px}
.vm h4{font-size:14px;font-weight:400;line-height:18px}
.vm p{font-family:"Open Sans",sans-serif;font-size:10px;color:var(--muted);line-height:18px;margin-top:10px;width:170px}

/* solution band */
.solution{top:1170px;height:417px;background:linear-gradient(120deg,#3d4754,#6c7784 50%,#3a4250);clip-path:polygon(0 16%,100% 0,100% 84%,0 100%);text-align:center;color:var(--white)}
.solution h2{margin-top:110px;font-size:28px;font-weight:600;line-height:44px}
.solution p{font-family:"Open Sans",sans-serif;font-size:12px;line-height:24px;margin-top:14px;opacity:.95}
.solution .btn{margin-top:18px;width:158px;padding:0}

/* products */
.products{top:1587px;height:849px;text-align:center}
.products .kicker{margin-top:103px}
.products h2{font-size:24px;font-weight:600;margin-top:4px}
.grid{position:absolute;left:103px;top:201px;display:grid;grid-template-columns:repeat(4,207px);column-gap:22px;row-gap:19px}
.card{height:252px;background:var(--white);box-shadow:0 3px 14px rgba(0,0,0,.08)}
.card .lab{height:48px;display:flex;align-items:center;justify-content:center;font-size:10px;line-height:13px;padding:0 10px}
.card .img{height:204px}
.img.dark{background:linear-gradient(160deg,#3b3f44,#111315)}
.img.light{background:linear-gradient(160deg,#e6e8eb,#c7ccd2)}
.img.grey{background:linear-gradient(160deg,#e0e2e6,#a8adb4)}
.products .btn{position:absolute;left:453px;top:767px;width:194px;padding:0;height:42px}

/* commitment */
.commit{top:2436px;height:440px;background:linear-gradient(110deg,#3a4556,#7b8796 55%,#c7cfd7);clip-path:polygon(0 15%,100% 0,100% 95%,0 100%);color:var(--white)}
.commit .k{position:absolute;left:157px;top:148px;font-size:12px}
.commit h2{position:absolute;left:157px;top:172px;font-size:26px;font-weight:400;line-height:32px;width:460px}
.commit p{position:absolute;left:157px;top:284px;width:440px;font-family:"Open Sans",sans-serif;font-size:11px;line-height:18px}
.commit .btn{position:absolute;left:814px;top:200px;width:182px;padding:0;height:42px}

/* stats */
.stats{top:2909px;left:103px;width:895px;height:161px;background:var(--blue);color:var(--white);display:grid;grid-template-columns:repeat(4,1fr);align-items:center;text-align:center}
.stat .n{font-size:40px;font-weight:300;line-height:46px}
.stat .n sup{font-size:26px;vertical-align:18px;margin-left:2px}
.stat .l{font-size:13px;margin-top:4px}

/* news */
.news{top:3150px;height:460px;text-align:center}
.news h2{font-size:24px;font-weight:600;margin-top:24px}
.newsgrid{position:absolute;left:103px;top:83px;display:grid;grid-template-columns:repeat(3,282px);column-gap:24px}
.newsgrid .img{height:167px}
.img.n1{background:linear-gradient(150deg,#9fb1c4,#58708b)}
.img.n2{background:linear-gradient(150deg,#b7bcc2,#5b6168)}
.img.n3{background:linear-gradient(150deg,#c9d3db,#8a7a66)}
.newsgrid h3{font-size:11px;font-weight:400;line-height:22px;margin-top:18px}
.newsgrid p{font-family:"Open Sans",sans-serif;font-size:10px;color:var(--muted);line-height:18px;margin-top:4px}
.news .btn{position:absolute;left:521px;top:387px;width:178px;padding:0;height:44px}

/* brands */
.brands{top:3645px;height:180px;text-align:center}
.brands h3{font-size:17px;font-weight:600}
.logos{position:absolute;left:103px;top:80px;width:895px;display:flex;justify-content:space-between;align-items:center}
.logos span{font-size:15px;font-weight:600;color:var(--ink);display:flex;align-items:center;gap:6px}
.logos i{display:inline-block;width:16px;height:16px;border-radius:50%;background:var(--ink)}

/* footer */
.footer{top:3786px;height:359px;background:var(--footer);clip-path:polygon(0 22%,100% 0,100% 100%,0 100%);color:#c6cbd2}
.fcol{position:absolute;top:118px}
.fcol h5{font-size:12px;font-weight:500;color:var(--white);letter-spacing:.3px}
.fcol ul{list-style:none;margin-top:14px}
.fcol li{font-size:10px;line-height:32px}
.fcol .txt{font-family:"Open Sans",sans-serif;font-size:10px;line-height:17px;margin-top:14px}
.fbrand{position:absolute;left:103px;top:114px}
.fbrand .row{display:flex;align-items:center;gap:10px}
.fbrand .mark{width:34px;height:34px;background:var(--white)}
.fbrand .name{font-size:30px;font-weight:600;color:var(--white)}
.fbrand p{font-family:"Open Sans",sans-serif;font-size:10px;line-height:20px;width:190px;margin-top:30px}
.social{display:flex;gap:14px;margin-top:14px}
.social i{width:14px;height:14px;border:1.5px solid #c6cbd2;border-radius:50%}
.copy{position:absolute;left:0;width:1100px;top:326px;text-align:center;font-size:10px}
</style>
</head>
<body>
<div class="site">

  <div class="sec topbar">
    <span class="item"><svg width="9" height="12" viewBox="0 0 9 12"><path d="M4.5 0A4.5 4.5 0 0 0 0 4.5C0 8 4.5 12 4.5 12S9 8 9 4.5A4.5 4.5 0 0 0 4.5 0zm0 6.3a1.8 1.8 0 1 1 0-3.6 1.8 1.8 0 0 1 0 3.6z" fill="#fff"/></svg>The 4th Industrial Park, Lanxi Town, Foshan</span>
    <span class="item"><svg width="12" height="10" viewBox="0 0 12 10"><rect x=".5" y=".5" width="11" height="9" fill="none" stroke="#fff"/><path d="M.5 .5 6 5.5 11.5.5" fill="none" stroke="#fff"/></svg>Email: info@valmoriqtech.com</span>
    <span class="links"><span>Careers</span><span class="sep">|</span><span>Quality Policy</span><span class="sep">|</span><span>Languages</span></span>
  </div>

  <div class="sec header">
    <div class="brand"><span class="mark"></span><div><div class="name">Valmoriq</div><small>Powering You Up For Success</small></div></div>
    <div class="phone">
      <svg width="24" height="24" viewBox="0 0 24 24"><path d="M6 2l4 4-2.5 2.5a13 13 0 0 0 8 8L18 14l4 4-3 3C10 21 3 14 3 5z" fill="none" stroke="#3176b5" stroke-width="1.5"/></svg>
      <div><div class="lab">24/7 Phone Services</div><div class="num">(86) 0755-41028300</div></div>
    </div>
  </div>

  <nav class="nav">
    <span>HOME</span><span>ABOUT US</span><span>INDUSTRIES</span><span>CORE COMPETENCIES</span><span>NEWS</span>
    <span class="quote">Get A Quote <svg width="12" height="8" viewBox="0 0 12 8"><path d="M0 4h11M8 1l3 3-3 3" stroke="#fff" fill="none"/></svg></span>
  </nav>

  <section class="sec hero" role="img" aria-label="Factory floor with production lines and workers">
    <div class="shade"></div>
    <div class="arrowc" style="left:52px"><svg width="8" height="12"><path d="M7 1 2 6l5 5" stroke="#fff" fill="none"/></svg></div>
    <div class="arrowc" style="left:1012px"><svg width="8" height="12"><path d="M1 1l5 5-5 5" stroke="#fff" fill="none"/></svg></div>
    <h1>We deliver quality<br>products at the fastest<br><b>speed to market.</b></h1>
    <p>Through our facilities in Asia and Europe, serving local and international customers ranging from SME to Fortune 500 companies</p>
    <span class="btn">Learn More <svg width="12" height="8"><path d="M0 4h11M8 1l3 3-3 3" stroke="#fff" fill="none"/></svg></span>
    <div class="play"><span class="c"><svg width="10" height="12"><path d="M1 1l8 5-8 5z" fill="none" stroke="#fff"/></svg></span><span>Watch<br>Our Video</span></div>
  </section>

  <section class="sec about">
    <div class="left">
      <svg width="34" height="46" viewBox="0 0 34 46"><g stroke="#3176b5" stroke-width="1.2"><path d="M2 10v30M9 4v38M16 8v34M23 2v42M30 12v26"/></g></svg>
      <div><div class="kicker">WELCOME TO VALMORIQ</div><h2>About<br>Our Company.</h2></div>
    </div>
    <div class="right">
      <div class="lead">Valmoriq is one of the top global suppliers of switches, electronic <b>modules and sensors.</b></div>
      <div class="body">Our parent company was founded in 1978 as a switch manufacturer in Hong Kong, the Valmoriq brand has achieved global recognition in various sectors. Over four decades later, we continue to facilitate...</div>
      <div class="vm">
        <div class="col">
          <svg width="44" height="34" viewBox="0 0 44 34"><ellipse cx="22" cy="17" rx="20" ry="12" fill="none" stroke="#3176b5" stroke-width="1.5"/><circle cx="22" cy="17" r="7" fill="none" stroke="#3176b5" stroke-width="1.5"/><circle cx="22" cy="17" r="2.5" fill="#3176b5"/></svg>
          <div><h4>Our<br>Vision</h4><p>Powering you up<br>for success.</p></div>
        </div>
        <div class="col">
          <svg width="36" height="36" viewBox="0 0 36 36"><path d="M18 3 4 33h28z" fill="none" stroke="#3176b5" stroke-width="1.5"/><path d="M18 3v-2h8v5h-8" fill="none" stroke="#3176b5" stroke-width="1.5"/></svg>
          <div><h4>Our<br>Mission</h4><p>To exceed customers' expectations with the most innovative technologies, the best cost effectiveness, and the utmost professional services.</p></div>
        </div>
      </div>
    </div>
  </section>

  <section class="sec solution" role="img" aria-label="Business meeting with hands, documents and a phone on a desk">
    <h2>We Provide customers with total solution<br>from initial design to manufacturing.</h2>
    <p>We offer original design, co-development and manufacturing services of<br>specialized switch and sensor based components and modules with top-notch</p>
    <span class="btn">Learn More <svg width="12" height="8"><path d="M0 4h11M8 1l3 3-3 3" stroke="#fff" fill="none"/></svg></span>
  </section>

  <section class="sec products">
    <div class="kicker">OUR PRODUCTS</div>
    <h2>Our Product Range</h2>
    <div class="grid">
      <div class="card"><div class="lab">Seat switches</div><div class="img dark" role="img" aria-label="Seat switch product photo"></div></div>
      <div class="card"><div class="lab">Door switches</div><div class="img dark" role="img" aria-label="Door switch panels product photo"></div></div>
      <div class="card"><div class="lab">Console switches</div><div class="img dark" role="img" aria-label="Console rotary switch product photo"></div></div>
      <div class="card"><div class="lab">Optical<br>Sensor Module</div><div class="img light" role="img" aria-label="Optical sensor module product photo"></div></div>
      <div class="card"><div class="lab">Encoder</div><div class="img light" role="img" aria-label="Encoder device product photo"></div></div>
      <div class="card"><div class="lab">Smart Touch<br>and Display Module</div><div class="img grey" role="img" aria-label="Smart touch display module product photo"></div></div>
      <div class="card"><div class="lab">Brushless<br>DC Controls</div><div class="img light" role="img" aria-label="Brushless DC control circuit board product photo"></div></div>
      <div class="card"><div class="lab">PM2.5 Air<br>Quality Sensor</div><div class="img light" role="img" aria-label="Air quality sensor housing product photo"></div></div>
    </div>
    <span class="btn">View All Products <svg width="12" height="8"><path d="M0 4h11M8 1l3 3-3 3" stroke="#fff" fill="none"/></svg></span>
  </section>

  <section class="sec commit" role="img" aria-label="Business team reviewing charts in an office">
    <div class="k">Reliable quality and service.</div>
    <h2>Our commitment to your success is our drive to continuous innovation and improvement.</h2>
    <p>Shorten your time to market, minimize overall cost, and attaining superior quality through our extensive experience in products.</p>
    <span class="btn">Learn more <svg width="12" height="8"><path d="M0 4h11M8 1l3 3-3 3" stroke="#fff" fill="none"/></svg></span>
  </section>

  <div class="sec stats">
    <div class="stat"><div class="n">18<sup>+</sup></div><div class="l">Yr Experience</div></div>
    <div class="stat"><div class="n">502<sup>+</sup></div><div class="l">Complete Projects</div></div>
    <div class="stat"><div class="n">120<sup>+</sup></div><div class="l">Works Employed</div></div>
    <div class="stat"><div class="n">12<sup>+</sup></div><div class="l">Running Projects</div></div>
  </div>

  <section class="sec news">
    <h2>Our Latest News</h2>
    <div class="newsgrid">
      <article><div class="img n1" role="img" aria-label="Delegation visiting the company showroom"></div><h3>Lanxi Robotics Association<br>visits Valmoriq</h3><p>A delegation led by Lanxi<br>Robotics Association visited Valmoriq...</p></article>
      <article><div class="img n2" role="img" aria-label="Automated material distribution system on a factory floor"></div><h3>Valmoriq's self-developed Intelligent<br>Material Distribution System granted</h3><p>Recently, Valmoriq self-developed<br>material distribution system was...</p></article>
      <article><div class="img n3" role="img" aria-label="Historic university building with trees"></div><h3>Valmoriq and academia join<br>forces to drive innovation</h3><p>In 2020, we are so privileged to<br>participate in a joint-research program...</p></article>
    </div>
    <span class="btn">View All News <svg width="12" height="8"><path d="M0 4h11M8 1l3 3-3 3" stroke="#fff" fill="none"/></svg></span>
  </section>

  <section class="sec brands">
    <h3>Brands we serve:</h3>
    <div class="logos">
      <span>Marwick Fenn &amp; Toller</span>
      <span>Tolvaro</span>
      <span><i></i>Pruvet</span>
      <span>Quenmatic</span>
      <span>Halvorne</span>
      <span><i></i>KRV</span>
    </div>
  </section>

  <footer class="sec footer">
    <div class="fbrand">
      <div class="row"><span class="mark"></span><span class="name">Valmoriq</span></div>
      <p>Lorem Ipsum is simply dummy text of the printing and typesetting industry. Lorem Ipsum has been.</p>
      <div class="social"><i></i><i></i><i></i></div>
    </div>
    <div class="fcol" style="left:343px"><h5>QUICK LINKS</h5><ul><li>About us</li><li>Industries</li><li>Core Competencies</li><li>News</li></ul></div>
    <div class="fcol" style="left:493px"><h5>CORE COMPETENCIES</h5><ul><li>Research &amp; Development</li><li>Manufacturing Capabilities</li><li>Process Management</li><li>Quality Management</li></ul></div>
    <div class="fcol" style="left:685px"><h5>INDUSTRIES</h5><ul><li>Automotive</li><li>Electrical &amp; Electronic</li><li>Power Tools</li><li>Sensors</li></ul></div>
    <div class="fcol" style="left:845px"><h5>CONTACT US</h5>
      <div class="txt">Valmoriq Electech Co., Ltd<br>The 4th Industrial Park,<br>Lanxi Town, Foshan City,<br>Guangdong Province, PRC<br><br>Email: info@valmoriqtech.com<br>Tel: (86) 0755-41028300<br>Fax: (86) 0755-41028399</div>
    </div>
    <div class="copy">Copyright © 2020 Valmoriq. All rights reserved.</div>
  </footer>

</div>
</body>
</html>
```